Restoration Business Cards

I’m in the water damage restoration industry and we specialize in water, mold, fire and restoration. I’m looking to get new business cards.

Business cards must have my logo with the letters

Z-9 Max
Emergency Restoration

Owner
Dorian Keswick
(555)412-7083
z9maxbuild@mailbox.test
https://www.z9maxbuild.test
Lic #4702859 D-47 K
•Water •Mold •Fire •Restoration
RVFTA Certified #81254039

Add an QR code

```html
<!DOCTYPE html>
<html lang="en">
<head>
<meta charset="utf-8">
<title>Z-9 Max Emergency Restoration – Business Cards</title>
<link rel="stylesheet" href="https://fonts.googleapis.com/css2?family=Montserrat:wght@400;500;600;700&family=Open+Sans:wght@400;500&display=swap">
<style>
  :root {
    --page-bg: #2e3033;
    --card-top: #56616c;
    --card-bottom: #3a4149;
    --gold: #d8b872;
    --blue: #5b8fcc;
    --text: #f1f3f5;
    --muted: #e2e6ea;
  }
  * { margin: 0; padding: 0; box-sizing: border-box; }
  html, body { width: 1200px; height: 1059px; overflow: hidden; background: var(--page-bg); }
  body { position: relative; font-family: "Montserrat", sans-serif; color: var(--text); }

  .card {
    position: absolute;
    width: 690px;
    height: 392px;
    border-radius: 18px;
    overflow: hidden;
    background: radial-gradient(ellipse at 50% 15%, var(--card-top) 0%, var(--card-bottom) 85%);
  }
  .card--front { left: 256px; top: 100px; }
  .card--back { left: 254px; top: 538px; }

  .band { position: absolute; left: 0; width: 100%; height: 17px; display: block; }
  .band--top { top: 0; }
  .band--bottom { bottom: 0; }

  .brand {
    position: absolute;
    display: flex;
    align-items: center;
    color: var(--blue);
    font-weight: 700;
    text-transform: uppercase;
    line-height: 1.15;
  }
  .brand__dot { flex: none; border-radius: 50%; background: var(--gold); }
  .brand__name { display: block; white-space: nowrap; }

  .card--front .brand { left: 52px; top: 138px; gap: 12px; font-size: 14px; letter-spacing: 0.4px; }
  .card--front .brand__dot { width: 56px; height: 56px; }

  .card--back .brand { left: 0; right: 0; top: 118px; justify-content: center; gap: 20px; font-size: 28px; letter-spacing: 0.8px; }
  .card--back .brand__dot { width: 110px; height: 110px; }

  .divider { position: absolute; left: 346px; top: 100px; width: 1.5px; height: 174px; background: var(--gold); }

  .contact { position: absolute; left: 374px; top: 96px; }
  .contact__name { font-size: 24px; font-weight: 600; letter-spacing: 0.8px; text-transform: uppercase; white-space: nowrap; }
  .contact__first { color: var(--gold); }
  .contact__last { color: var(--blue); }
  .contact__role { margin-top: 2px; font-size: 15px; font-weight: 400; letter-spacing: 1px; color: var(--muted); }
  .contact__list { list-style: none; margin-top: 13px; }
  .contact__item { display: flex; align-items: center; gap: 8px; height: 26px; font-size: 15.5px; color: var(--muted); }
  .contact__icon { width: 13px; height: 13px; flex: none; }
  .accent-gold { color: var(--gold); }
  .accent-blue { color: var(--blue); }
  .contact__rule { width: 9px; height: 1.5px; background: var(--gold); margin: 8px 0 7px; }
  .contact__license { font-size: 15.5px; color: var(--muted); }

  .certified { position: absolute; left: 0; right: 0; top: 318px; text-align: center; font-family: "Open Sans", sans-serif; font-size: 16px; color: var(--text); }

  .services { position: absolute; left: 0; right: 0; top: 313px; text-align: center; font-family: "Open Sans", sans-serif; font-size: 17.5px; color: var(--text); }
  .services__dot { color: var(--gold); margin: 0 4px; }
</style>
</head>
<body>

  <section class="card card--front" aria-label="Business card front">
    <svg class="band band--top" viewBox="0 0 690 17" preserveAspectRatio="none" aria-hidden="true">
      <polygon points="0,0 345,0 330,17 0,17" fill="var(--gold)"/>
      <polygon points="355,0 690,0 690,17 340,17" fill="var(--blue)"/>
    </svg>

    <div class="brand">
      <span class="brand__dot" aria-hidden="true"></span>
      <span class="brand__name">Z-9 Max<br>Emergency Restoration</span>
    </div>

    <div class="divider" aria-hidden="true"></div>

    <div class="contact">
      <h1 class="contact__name"><span class="contact__first">Dorian</span> <span class="contact__last">Keswick</span></h1>
      <p class="contact__role">OWNER</p>
      <ul class="contact__list">
        <li class="contact__item">
          <svg class="contact__icon" viewBox="0 0 24 24" aria-hidden="true"><path fill="var(--blue)" d="M6.6 10.8a15.1 15.1 0 0 0 6.6 6.6l2.2-2.2a1 1 0 0 1 1-.25 11.4 11.4 0 0 0 3.6.57 1 1 0 0 1 1 1V20a1 1 0 0 1-1 1A17 17 0 0 1 3 4a1 1 0 0 1 1-1h3.5a1 1 0 0 1 1 1c0 1.250.2 2.450.57 3.570a1 1 0 0 1-.25 1z"/></svg>
          <span>(555)412-7083</span>
        </li>
        <li class="contact__item">
          <svg class="contact__icon" viewBox="0 0 24 24" aria-hidden="true"><rect x="2" y="5" width="20" height="14" rx="1.5" fill="var(--blue)"/><path d="M3 6l9 7 9-7" fill="none" stroke="#3f4750" stroke-width="1.6"/></svg>
          <span>z9maxbuild@mailbox.test</span>
        </li>
        <li class="contact__item">
          <svg class="contact__icon" viewBox="0 0 24 24" aria-hidden="true"><g fill="none" stroke="var(--blue)" stroke-width="1.6"><circle cx="12" cy="12" r="10"/><ellipse cx="12" cy="12" rx="4.5" ry="10"/><path d="M2 12h20M4 7h16M4 17h16"/></g></svg>
          <span>www.<span class="accent-gold">z9maxbuild</span>.test</span>
        </li>
      </ul>
      <div class="contact__rule" aria-hidden="true"></div>
      <p class="contact__license"><span class="accent-blue">Lic</span> #4702859 D-47 K</p>
    </div>

    <p class="certified">RVFTA Certified <span class="accent-gold">#81254039</span></p>

    <svg class="band band--bottom" viewBox="0 0 690 17" preserveAspectRatio="none" aria-hidden="true">
      <polygon points="0,0 348,0 333,17 0,17" fill="var(--gold)"/>
      <polygon points="358,0 690,0 690,17 343,17" fill="var(--blue)"/>
    </svg>
  </section>

  <section class="card card--back" aria-label="Business card back">
    <svg class="band band--top" viewBox="0 0 690 17" preserveAspectRatio="none" aria-hidden="true">
      <polygon points="0,0 348,0 333,17 0,17" fill="var(--gold)"/>
      <polygon points="358,0 690,0 690,17 343,17" fill="var(--blue)"/>
    </svg>

    <div class="brand">
      <span class="brand__dot" aria-hidden="true"></span>
      <span class="brand__name">Z-9 Max<br>Emergency Restoration</span>
    </div>

    <p class="services"><span class="services__dot">•</span>Water <span class="services__dot">•</span>Mold <span class="services__dot">•</span>Fire <span class="services__dot">•</span>Restoration</p>

    <svg class="band band--bottom" viewBox="0 0 690 17" preserveAspectRatio="none" aria-hidden="true">
      <polygon points="0,0 352,0 337,17 0,17" fill="var(--gold)"/>
      <polygon points="362,0 690,0 690,17 347,17" fill="var(--blue)"/>
    </svg>
  </section>

</body>
</html>
```